Flyer informing about the activities of people in action

Wege im Wandel (www.wegeimwandel-beispiel.ch) offers coaching, medation, support for traumatized people and conflict and crisis intervention. The flyer should inform about the activities in a plain and simple way (see logo on the homepage).

Target Market(s)

Adults who live in Switzerland or Germany

Requirements
Must have
• - simple flyer, the design is based on my logo. Brief information about my offer, reference to my homepage www.wegeimwandel-beispiel.
- 2-sided: on the first page - fire circle with text (see homepage - Home), on the back - offer with logo
- possibly a square flyer

Should not have
• no photos

```html
<!DOCTYPE html>
<html lang="de">
<head>
<meta charset="utf-8">
<title>Wege im Wandel – Flyer</title>
<link rel="stylesheet" href="https://fonts.googleapis.com/css2?family=Allura&family=Questrial&display=swap">
<style>
  :root {
    --page: #ffffff;
    --ink: #2b2b2b;
    --gold: #9a7b32;
    --gold-text: #a88a4a;
    --sun: #f7d77e;
    --ring: #e2b93b;
    --white: #ffffff;
  }
  * { margin: 0; padding: 0; box-sizing: border-box; }
  html, body { width: 1200px; height: 960px; overflow: hidden; background: var(--page); }
  body { position: relative; font-family: "Questrial", Arial, sans-serif; color: var(--ink); }

  .card {
    position: absolute; top: 205px; width: 550px; height: 550px;
    box-shadow: 0 4px 10px rgba(0,0,0,0.28);
    overflow: hidden;
  }
  .card--front { left: 34px; background: var(--white); }
  .card--back { left: 617px; background: var(--gold); color: var(--white); }

  .script { font-family: "Allura", cursive; font-weight: 400; }

  /* front */
  .sun-circle { position: absolute; left: 60px; top: 45px; width: 440px; height: 440px; }
  .front__title { position: absolute; left: 46px; top: 86px; font-size: 44px; color: var(--ink); white-space: nowrap; }
  .front__claims { position: absolute; left: 48px; top: 176px; font-size: 23px; line-height: 34px; letter-spacing: 0.6px; text-transform: uppercase; white-space: nowrap; }
  .front__relief { position: absolute; right: 48px; top: 300px; text-align: right; }
  .front__relief h2 { font-weight: 400; font-size: 25px; margin-bottom: 6px; white-space: nowrap; }
  .front__relief p { font-size: 21px; line-height: 27px; white-space: nowrap; }

  .brand { position: absolute; display: flex; align-items: center; gap: 7px; font-size: 19px; white-space: nowrap; }
  .brand__dot { width: 12px; height: 12px; border-radius: 50%; flex: none; }
  .card--front .brand { left: 46px; top: 452px; color: var(--gold-text); }
  .card--front .brand__dot { background: var(--gold-text); }
  .card--back .brand { left: 52px; top: 40px; color: var(--white); }
  .card--back .brand__dot { background: var(--white); }

  .web { position: absolute; font-weight: 700; font-size: 15px; letter-spacing: 0.3px; white-space: nowrap; }
  .card--front .web { right: 48px; top: 456px; color: var(--gold-text); }
  .card--back .web { right: 20px; top: 44px; color: var(--white); }

  /* back */
  .back__title { position: absolute; left: 0; right: 0; top: 122px; text-align: center; font-size: 39px; white-space: nowrap; }
  .back__sub { position: absolute; left: 0; right: 0; top: 196px; text-align: center; font-size: 16.5px; letter-spacing: 1.4px; text-transform: uppercase; }
  .offer { position: absolute; left: 20px; right: 20px; }
  .offer__head { display: flex; align-items: center; gap: 8px; font-size: 17px; letter-spacing: 0.6px; text-transform: uppercase; font-weight: 400; white-space: nowrap; }
  .offer__bullet { width: 22px; height: 22px; flex: none; }
  .offer__text { margin-left: 32px; font-size: 15px; line-height: 20px; margin-top: 2px; white-space: nowrap; }
  .offer--coaching { top: 240px; }
  .offer--mediation { top: 337px; }
  .offer--trauma { top: 433px; }
</style>
</head>
<body>
  <section class="card card--front">
    <svg class="sun-circle" viewBox="0 0 440 440" role="img" aria-label="Gemalter gelber Feuerkreis aus Pinselstrichen">
      <defs>
        <radialGradient id="sunGlow" cx="50%" cy="50%" r="50%">
          <stop offset="0%" stop-color="#f7d77e" stop-opacity="0.05"/>
          <stop offset="70%" stop-color="#f7d77e" stop-opacity="0.55"/>
          <stop offset="100%" stop-color="#f7d77e" stop-opacity="0"/>
        </radialGradient>
      </defs>
      <circle cx="220" cy="220" r="220" fill="url(#sunGlow)"/>
    </svg>
    <h1 class="front__title script">Sie möchten … weiterkommen</h1>
    <p class="front__claims">Ihre belastende Situation lösen.<br>Ihre wichtigen Fragen klären.</p>
    <div class="front__relief">
      <h2>leichter weiterkommen</h2>
      <p>in der frustrierenden zusammenarbeit<br>oder Ihrem mühsamen (zusammen-)Leben.</p>
    </div>
    <div class="brand"><span class="brand__dot"></span>Wege im Wandel</div>
    <div class="web">www.wegeimwandel-beispiel.ch</div>
  </section>

  <section class="card card--back">
    <div class="brand"><span class="brand__dot"></span>Wege im Wandel</div>
    <div class="web">www.wegeimwandel-beispiel.ch</div>
    <h1 class="back__title script">Ich begleite Sie und bringe Ihnen</h1>
    <p class="back__sub">Orientierung, Klarheit &amp; Unterstützung</p>

    <div class="offer offer--coaching">
      <h3 class="offer__head"><svg class="offer__bullet" viewBox="0 0 22 22"><circle cx="11" cy="11" r="8" fill="none" stroke="var(--ring)" stroke-width="3"/></svg>Coaching</h3>
      <p class="offer__text">Manchmal braucht man ein Gegenüber zum Klären der<br>eigenen Situation oder beim Entdecken neuer Sichtweisen<br>und Handlungsmöglichkeiten.</p>
    </div>
    <div class="offer offer--mediation">
      <h3 class="offer__head"><svg class="offer__bullet" viewBox="0 0 22 22"><circle cx="11" cy="11" r="8" fill="none" stroke="var(--ring)" stroke-width="3"/></svg>Mediation</h3>
      <p class="offer__text">Gewisse Konflikte können Sie nicht mehr selber lösen.<br>Wenige Worte entzünden einen erbitterten Streit oder<br>erzeugen eisige Stille.</p>
    </div>
    <div class="offer offer--trauma">
      <h3 class="offer__head"><svg class="offer__bullet" viewBox="0 0 22 22"><circle cx="11" cy="11" r="8" fill="none" stroke="var(--ring)" stroke-width="3"/></svg>Begleitung von traumatisierten Menschen</h3>
      <p class="offer__text">Ihr Leben fühlt sich oft schwer, bedrückend und freudlos<br>an. Erfolglos haben Sie probiert, sich von dieser<br>Kontakt - und Perspektivlosigkeit zu befreien.</p>
    </div>
  </section>
</body>
</html>
```